professional business card

A Clean looking business card for a money transfer company. Our company is call Velorix= Transfer + Send = Transcend (next level)
to show professionalism as well as some effects to show digital tech.

1 side to have position, name and address
2 side to have company name and show that we provide money exchange and cross-border money transfer

Target Market(s)

Remittance companies and high net worth individuals

Industry/Entity Type

Finance

Contact Information for Business Card

Name, address, email, title, services- money exchange and cross-border remittance

Requirements
Nice to have
• Digital age feel

```html
<!DOCTYPE html>
<html lang="en">
<head>
<meta charset="UTF-8">
<title>Velorix Business Card</title>
<link href="https://fonts.googleapis.com/css2?family=Montserrat:wght@400;500;600;700&display=swap" rel="stylesheet">
<style>
  :root {
    --page-bg: #e8e9ea;
    --card-navy: #263341;
    --card-shade: #324150;
    --teal: #5cc3d4;
    --white: #ffffff;
    --soft-white: #e6ebef;
  }
  * { box-sizing: border-box; margin: 0; padding: 0; }
  html, body {
    width: 1200px;
    height: 900px;
    overflow: hidden;
    background: var(--page-bg);
    font-family: "Montserrat", sans-serif;
  }
  .canvas {
    position: relative;
    width: 1200px;
    height: 900px;
  }
  .card {
    position: absolute;
    width: 700px;
    height: 400px;
    background: var(--card-navy);
    overflow: hidden;
    box-shadow: 0 6px 18px rgba(30, 40, 50, 0.18);
  }
  .card--front { left: 80px; top: 40px; }
  .card--back { left: 420px; top: 460px; }

  .brand {
    display: flex;
    align-items: center;
    gap: 14px;
    color: var(--white);
    font-weight: 500;
    text-transform: uppercase;
    letter-spacing: 0.04em;
  }
  .brand__mark {
    background: var(--teal);
    flex: none;
  }

  /* Front */
  .card--front .brand {
    position: absolute;
    left: 150px;
    top: 128px;
    font-size: 64px;
  }
  .card--front .brand__mark { width: 44px; height: 44px; }
  .tagline {
    position: absolute;
    left: 152px;
    top: 232px;
    font-size: 17.5px;
    font-weight: 600;
    color: var(--white);
    letter-spacing: 0.01em;
  }
  .tagline__accent { color: var(--teal); }

  /* Back */
  .card--back .brand {
    position: absolute;
    left: 48px;
    top: 56px;
    font-size: 40px;
  }
  .card--back .brand__mark { width: 28px; height: 28px; }
  .divider {
    position: absolute;
    left: 48px;
    right: 48px;
    top: 178px;
    height: 1.5px;
    background: var(--teal);
  }
  .person {
    position: absolute;
    left: 48px;
    top: 120px;
  }
  .person__name {
    font-size: 26px;
    font-weight: 700;
    color: var(--teal);
    letter-spacing: 0.01em;
  }
  .person__title {
    margin-top: 8px;
    font-size: 17px;
    font-weight: 400;
    color: var(--soft-white);
  }
  .person { top: 112px; }
  .divider { top: 196px; left: 48px; right: 48px; }
  .contact-list {
    position: absolute;
    left: 48px;
    top: 220px;
    list-style: none;
  }
  .contact-list__item {
    display: flex;
    align-items: center;
    gap: 12px;
    font-size: 17px;
    color: var(--soft-white);
    line-height: 34px;
    letter-spacing: 0.02em;
  }
  .contact-list__icon {
    width: 16px;
    height: 16px;
    flex: none;
  }
  .address {
    position: absolute;
    right: 48px;
    top: 300px;
    text-align: right;
    font-size: 16px;
    line-height: 26px;
    color: var(--soft-white);
    letter-spacing: 0.02em;
  }
</style>
</head>
<body>
<main class="canvas">

  <section class="card card--front" aria-label="Card front">
    <div class="brand">
      <span class="brand__mark"></span>
      <span class="brand__name">Velorix</span>
    </div>
    <p class="tagline">we provide money <span class="tagline__accent">exchange and cross-border</span> money transfer</p>
  </section>

  <section class="card card--back" aria-label="Card back">
    <div class="brand">
      <span class="brand__mark"></span>
      <span class="brand__name">Velorix</span>
    </div>

    <div class="person">
      <p class="person__name">Lorena Vasquel</p>
      <p class="person__title">CEO/Founder</p>
    </div>

    <div class="divider"></div>

    <ul class="contact-list">
      <li class="contact-list__item">
        <svg class="contact-list__icon" viewBox="0 0 16 16" aria-hidden="true">
          <path d="M3 1.5l3 3-1.6 1.6c.8 1.9 2.4 3.5 4.3 4.3L10.3 8.8l3 3-1.8 1.9C6.6 13.4 2.4 9.2 1.2 3.4z" fill="var(--teal)"/>
        </svg>
        555.210.4837
      </li>
      <li class="contact-list__item">
        <svg class="contact-list__icon" viewBox="0 0 16 16" aria-hidden="true">
          <rect x="4" y="1" width="8" height="14" rx="1.5" fill="none" stroke="var(--teal)" stroke-width="1.6"/>
          <circle cx="8" cy="12.3" r="0.9" fill="var(--teal)"/>
        </svg>
        555.906.1274
      </li>
      <li class="contact-list__item">
        <svg class="contact-list__icon" viewBox="0 0 16 16" aria-hidden="true">
          <rect x="1" y="3.5" width="14" height="9.5" rx="1" fill="var(--teal)"/>
          <path d="M1.5 4l6.5 5 6.5-5" fill="none" stroke="var(--card-navy)" stroke-width="1.3"/>
        </svg>
        info@velorix.com
      </li>
      <li class="contact-list__item">
        <svg class="contact-list__icon" viewBox="0 0 16 16" aria-hidden="true">
          <circle cx="8" cy="8" r="6.5" fill="none" stroke="var(--teal)" stroke-width="1.5"/>
          <ellipse cx="8" cy="8" rx="2.8" ry="6.5" fill="none" stroke="var(--teal)" stroke-width="1.2"/>
          <line x1="1.5" y1="8" x2="14.5" y2="8" stroke="var(--teal)" stroke-width="1.2"/>
        </svg>
        www.velorix.com
      </li>
    </ul>

    <address class="address" style="font-style: normal;">
      P.O Box 7310 Harbour Lane<br>
      Westmere AB 2047
    </address>
  </section>

</main>
</body>
</html>
```